CREATE A BUSINESS CARD FOR A BOAT CLEANING SERVICE

WE ARE STARTING A NEW BOAT CLEANING BUSINESS. WE DIVE UNDERWATER TO CLEAN BOAT HULLS, JETTIES, UNDERWATER STRUCTURES ETC. WE ARE LOOKING FOR AN UPPERMARKET MODERN LOGO AND BUSINESS CARD AS ALOT OF OUR TARGET MARKET WILL BE HIGH END. YOU HAVE TO DESIGN A BUSINESS CARD AND LOGO SEPERATELY .
THE BUSINESS CARD DIMESNION MUST BE STANDARD SIZE.
The standard dimensions of a printed business card are 3.5 x 2 inches

Target Market(s)

UNDERWATER SERVICED

Industry/Entity Type

Business

Contact Information for Business Card

HALDANE SUBSEA SERVICES

Font styles to use
Serif

Colors

Designer to choose colors to be used in the design.

Requirements
Must have
• HALDANE
Nice to have
• dark
Should not have
• more than 3 colors

```html
<!DOCTYPE html>
<html lang="en">
<head>
<meta charset="utf-8">
<title>Haldane Subsea Services – Business Card</title>
<link rel="stylesheet" href="https://fonts.googleapis.com/css2?family=Open+Sans:wght@400;600;700&display=swap">
<style>
  :root {
    --bg: #d9dcdc;
    --teal-light: #0a86a8;
    --teal-mid: #0a6a8a;
    --teal-deep: #0b3a55;
    --navy: #1c2e45;
    --white: #ffffff;
    --shadow: rgba(0, 0, 0, 0.35);
  }
  * { margin: 0; padding: 0; box-sizing: border-box; }
  html, body {
    width: 1200px;
    height: 900px;
    overflow: hidden;
    background: var(--bg);
    font-family: "Open Sans", Arial, sans-serif;
  }
  .canvas {
    position: relative;
    width: 1200px;
    height: 900px;
  }
  .card {
    position: absolute;
    width: 520px;
    height: 297px;
    overflow: hidden;
    box-shadow: 4px 6px 12px var(--shadow);
  }
  /* Front side */
  .card-front {
    left: 80px;
    top: 150px;
    background: linear-gradient(135deg, var(--teal-light) 0%, var(--teal-mid) 40%, var(--teal-deep) 100%);
  }
  .wordmark {
    position: absolute;
    left: 0;
    right: 0;
    text-align: center;
    color: var(--navy);
    font-weight: 700;
    white-space: nowrap;
  }
  .card-front .brand-name {
    top: 112px;
    font-size: 40px;
    letter-spacing: 14px;
    padding-left: 14px;
  }
  .card-front .brand-tagline {
    top: 166px;
    font-size: 15px;
    letter-spacing: 5px;
    padding-left: 5px;
  }
  /* Back side */
  .card-back {
    left: 600px;
    top: 440px;
    background: var(--white);
  }
  .card-back .brand-name {
    top: 56px;
    font-size: 22px;
    letter-spacing: 6px;
    padding-left: 6px;
  }
  .card-back .brand-tagline {
    top: 86px;
    font-size: 9px;
    letter-spacing: 2.5px;
    padding-left: 2.5px;
  }
  .contact-band {
    position: absolute;
    left: 0;
    top: 196px;
    width: 520px;
    height: 101px;
    background: linear-gradient(135deg, var(--teal-light) 0%, var(--teal-mid) 45%, var(--teal-deep) 100%);
  }
  .person {
    position: absolute;
    left: 58px;
    top: 240px;
  }
  .person-name {
    color: var(--navy);
    font-weight: 700;
    font-size: 22px;
    line-height: 1;
    white-space: nowrap;
  }
  .person-role {
    color: var(--white);
    font-size: 10px;
    margin-top: 5px;
    padding-left: 36px;
  }
  .contacts {
    position: absolute;
    left: 300px;
    top: 212px;
    list-style: none;
    color: var(--white);
    font-size: 11.5px;
  }
  .contacts li {
    display: flex;
    align-items: center;
    gap: 9px;
    height: 19px;
    white-space: nowrap;
  }
  .contacts svg {
    width: 9px;
    height: 9px;
    fill: var(--navy);
  }
</style>
</head>
<body>
<main class="canvas">

  <section class="card card-front" aria-label="Business card front">
    <div class="wordmark brand-name">HALDANE</div>
    <div class="wordmark brand-tagline">SUBSEA SERVICES</div>
  </section>

  <section class="card card-back" aria-label="Business card back">
    <div class="contact-band" role="img" aria-label="Decorative teal wave band across the lower part of the card"></div>

    <div class="wordmark brand-name">HALDANE</div>
    <div class="wordmark brand-tagline">SUBSEA SERVICES</div>

    <div class="person">
      <div class="person-name">MARK DALTON</div>
      <div class="person-role">General Manager</div>
    </div>

    <ul class="contacts">
      <li>
        <svg viewBox="0 0 10 10" aria-hidden="true"><circle cx="5" cy="5" r="4.5"/><circle cx="5" cy="5" r="1.8" fill="#0a6a8a"/></svg>
        dalton@haldanesubsea.com
      </li>
      <li>
        <svg viewBox="0 0 10 10" aria-hidden="true"><path d="M2,0.5 L3.8,2.8 L2.8,4 C3.5,5.5 4.5,6.5 6,7.2 L7.2,6.2 L9.5,8 L8.2,9.5 C4,9 1,6 0.5,1.8 Z"/></svg>
        021 487 330 912
      </li>
      <li>
        <svg viewBox="0 0 10 10" aria-hidden="true"><path d="M5,0.5 L9.5,5 L8,5 L8,9.5 L6,9.5 L6,6.5 L4,6.5 L4,9.5 L2,9.5 L2,5 L0.5,5 Z"/></svg>
        www.haldanesubsea.com
      </li>
    </ul>
  </section>

</main>
</body>
</html>
```